Pharmacy ad

need 2 pharmacy ads for the phone book. one for Birchfield Pharmacy and one for Corvane Rx Pharmacy. Dimensions for ad is 4.75in x 4.667 in. please see attached examples of ad uploaded as well logos of each pharmacy

```html
<!DOCTYPE html>
<html lang="en">
<head>
<meta charset="utf-8">
<title>Birchfield Pharmacy – Directory Ad</title>
<link href="https://fonts.googleapis.com/css2?family=Lato:ital,wght@0,300;0,400;0,700;0,900;1,400;1,900&family=Roboto+Condensed:ital,wght@0,300;0,400;0,700;1,700&display=swap" rel="stylesheet">
<style>
  :root {
    --page-bg: #ececec;
    --frame-green: #6cc04a;
    --brand-green: #64a844;
    --rule-green: #9fd47f;
    --navy: #1f1f4f;
    --ink: #1d1d3a;
    --sun-yellow: #f6cf00;
    --tick-yellow: #f3c300;
    --muted-green: #6c8f5c;
    --social-blue: #3a4f9e;
    --white: #ffffff;
  }
  * { box-sizing: border-box; margin: 0; padding: 0; }
  html, body { width: 1200px; height: 1000px; overflow: hidden; background: var(--page-bg); }
  .canvas { position: relative; width: 1200px; height: 1000px; }

  .ad {
    position: absolute; left: 250px; top: 137px; width: 724px; height: 712px;
    background: var(--white); border: 12px solid var(--frame-green);
  }
  .ad > * { position: absolute; }

  .brand { left: 36px; top: 16px; width: 200px; text-align: center; }
  .brand-mark { width: 80px; height: 80px; border-radius: 50%; background: var(--sun-yellow); margin: 0 auto 14px; }
  .brand-name {
    font-family: "Lato", sans-serif; font-weight: 900; color: var(--navy);
    font-size: 30px; line-height: 34px; letter-spacing: .3px; text-transform: uppercase;
  }
  .brand-tag { font-family: "Lato", sans-serif; font-style: italic; font-size: 11px; line-height: 14px; color: var(--brand-green); margin-top: 6px; }

  .info {
    right: 16px; top: 16px; text-align: right; font-style: normal;
    font-family: "Roboto Condensed", sans-serif; font-size: 16.5px; color: var(--ink); line-height: 25.5px;
  }
  .info .phone { font-weight: 700; font-size: 17px; }

  .rule { height: 1px; background: var(--rule-green); }
  .rule-a { left: 26px; width: 646px; top: 209px; }
  .rule-b { left: 26px; width: 646px; top: 289px; }
  .rule-c { left: 30px; width: 646px; top: 501px; }
  .rule-d { left: 30px; width: 646px; top: 633px; }

  .headline {
    left: 0; width: 700px; top: 214px; text-align: center;
    font-family: "Lato", sans-serif; font-weight: 900; font-style: italic;
    font-size: 57px; line-height: 68px; color: var(--brand-green); letter-spacing: -.8px;
  }

  .services { top: 322px; display: grid; gap: 6px; list-style: none; }
  .services-left { left: 36px; }
  .services-right { left: 286px; }
  .services li {
    display: flex; align-items: center; gap: 14px; height: 30px;
    font-family: "Roboto Condensed", sans-serif; font-weight: 300; font-size: 25px; color: var(--brand-green);
  }
  .tick { width: 28px; height: 24px; flex: none; }

  .discount-figure {
    left: 58px; top: 500px; font-family: "Lato", sans-serif; font-weight: 900;
    font-size: 122px; line-height: 130px; color: var(--sun-yellow); letter-spacing: -3px;
  }
  .discounts { left: 315px; top: 520px; font-family: "Lato", sans-serif; }
  .discount-title { font-weight: 900; font-size: 25px; line-height: 28px; color: var(--brand-green); }
  .discount-note { font-size: 18px; line-height: 22px; color: var(--muted-green); margin-bottom: 8px; }

  .payments { left: 34px; top: 650px; display: flex; align-items: center; gap: 16px; font-family: "Lato", sans-serif; }
  .payments-label { font-weight: 300; font-size: 25px; color: var(--brand-green); margin-right: 8px; }
  .payment-name { font-size: 11px; font-weight: 700; color: var(--ink); }

  .social {
    right: 0; top: 653px; width: 199px; height: 34px;
    background: var(--social-blue); clip-path: polygon(14px 0, 100% 0, 100% 100%, 0 100%);
    display: flex; align-items: center; justify-content: flex-end; padding-right: 12px;
    font-family: "Roboto Condensed", sans-serif; font-weight: 700; font-style: italic;
    font-size: 16px; color: var(--white);
  }
</style>
</head>
<body>
<div class="canvas">
  <section class="ad">
    <div class="brand">
      <div class="brand-mark"></div>
      <div class="brand-name">Birchfield<br>Pharmacy</div>
      <div class="brand-tag">We Care About Your Health</div>
    </div>

    <address class="info">
      Monday – Friday 10am- 6pm<br>
      Saturday 10am-5pm &nbsp;|&nbsp; Sunday 10am-2pm (Marlow Street branch)<br>
      19 Marlow Street, Kestrelton (opposite Greenhill Chapel)<br>
      Harbour Point, Food Court, Kestrelton<br>
      <span class="phone">Phone: 555- 0142</span>
    </address>

    <div class="rule rule-a"></div>
    <h1 class="headline">We Care About Your Health</h1>
    <div class="rule rule-b"></div>

    <ul class="services services-left">
      <li><svg class="tick" viewBox="0 0 28 24"><path d="M3 13 L11 21 L26 3" fill="none" stroke="var(--tick-yellow)" stroke-width="4.5" stroke-linecap="round" stroke-linejoin="round"/></svg>Affordable prices</li>
      <li><svg class="tick" viewBox="0 0 28 24"><path d="M3 13 L11 21 L26 3" fill="none" stroke="var(--tick-yellow)" stroke-width="4.5" stroke-linecap="round" stroke-linejoin="round"/></svg>Injectables</li>
      <li><svg class="tick" viewBox="0 0 28 24"><path d="M3 13 L11 21 L26 3" fill="none" stroke="var(--tick-yellow)" stroke-width="4.5" stroke-linecap="round" stroke-linejoin="round"/></svg>Special Orders</li>
      <li><svg class="tick" viewBox="0 0 28 24"><path d="M3 13 L11 21 L26 3" fill="none" stroke="var(--tick-yellow)" stroke-width="4.5" stroke-linecap="round" stroke-linejoin="round"/></svg>Delivery service</li>
    </ul>
    <ul class="services services-right">
      <li><svg class="tick" viewBox="0 0 28 24"><path d="M3 13 L11 21 L26 3" fill="none" stroke="var(--tick-yellow)" stroke-width="4.5" stroke-linecap="round" stroke-linejoin="round"/></svg>Certified Pharmacists</li>
      <li><svg class="tick" viewBox="0 0 28 24"><path d="M3 13 L11 21 L26 3" fill="none" stroke="var(--tick-yellow)" stroke-width="4.5" stroke-linecap="round" stroke-linejoin="round"/></svg>Brand and Generic Medicines</li>
      <li><svg class="tick" viewBox="0 0 28 24"><path d="M3 13 L11 21 L26 3" fill="none" stroke="var(--tick-yellow)" stroke-width="4.5" stroke-linecap="round" stroke-linejoin="round"/></svg>Blood Pressure and Glucose checks</li>
      <li><svg class="tick" viewBox="0 0 28 24"><path d="M3 13 L11 21 L26 3" fill="none" stroke="var(--tick-yellow)" stroke-width="4.5" stroke-linecap="round" stroke-linejoin="round"/></svg>Personal care and Beauty Products</li>
    </ul>

    <div class="rule rule-c"></div>
    <div class="discount-figure">10%</div>
    <div class="discounts">
      <div class="discount-title">SENIOR CITIZEN DISCOUNT</div>
      <div class="discount-note">(For patients 60 years and over)</div>
      <div class="discount-title">STUDENT DISCOUNT</div>
      <div class="discount-note">(With valid ID card)</div>
    </div>
    <div class="rule rule-d"></div>

    <div class="payments">
      <span class="payments-label">We accept</span>
      <span class="payment-name">CardOne</span>
      <span class="payment-name">PayLine</span>
      <span class="payment-name">Meridia</span>
      <span class="payment-name">Ashcove</span>
    </div>
    <div class="social">Visit us on Friendspace</div>
  </section>
</div>
</body>
</html>
```